Webdesign

We are value investment firm in Denver, Colorado. We are a small but a very unique firm. We are looking for a minimalistic and clean design. We are competing against competitors that usually larger than we are, but we need to have a design that is better than theirs. Our clients put a tremendous trust in us when they let us manage their life savings. This website has to communicate trust but without traditional cliches (dollar bills, glasses, Harbor Ledger Gazette).
We had a coder/designer create our current website a few weeks ago http://brightkestrel.example/tolvan , we are not thrilled about the design. We are attaching our company's presentation, we'd like the design to be closer to the colors of that presentation.
We are looking for both design and coding (wordpress).
Updates
we will pay additional $200 for wordpress implementation
A few points of clarifications about design:
- don't use pictures of strangers
- we are a Denver/Colorado firm, if you use pictures use Denver/Colorado pictures
- full width website is probably what we are looking
- maybe parallax type of design
This theme http://quillframe.example/WP/Nimbra/ is how we see the new design
Industry/Entity Type
Investment

```html
<!DOCTYPE html>
<html lang="en">
<head>
<meta charset="utf-8">
<title>Tolvan – Investment Process</title>
<link href="https://fonts.googleapis.com/css2?family=Arimo:wght@400;700&family=Open+Sans:wght@400;600&family=Roboto:wght@900&family=Oswald:wght@300;600&display=swap" rel="stylesheet">
<style>
  :root{
    --navy:#1a3350;
    --ink:#2a3a4f;
    --nav:#3a3a3a;
    --slide-blue:#7aa6cf;
    --slide-deep:#2f5f8f;
    --brand-blue:#1c3f73;
    --bar:#ececec;
    --footer:#000;
    --footer-text:#b9b9b9;
  }
  *{margin:0;padding:0;box-sizing:border-box}
  html,body{width:1200px;height:1146px;overflow:hidden;background:#fff}
  body{position:relative;font-family:"Arimo",Arial,sans-serif;color:var(--nav)}
  .abs{position:absolute}

  .brand{left:177px;top:38px;display:flex;align-items:center;gap:8px;font-family:"Open Sans",sans-serif;font-weight:600;font-size:26px;color:var(--brand-blue)}
  .brand-mark{width:14px;height:14px;background:var(--brand-blue)}

  .follow{left:806px;top:31px;font-size:10px;letter-spacing:.2px}
  .social{top:19px;width:32px;height:32px;border:2px solid #cfcfcf;border-radius:50%}

  .nav{top:75px;left:0;width:1200px;font-size:13px;color:var(--nav)}
  .nav span{position:absolute;white-space:nowrap}

  .hero{left:0;top:117px;width:1200px;height:251px;background:var(--navy);overflow:hidden}
  .hero-photo{position:absolute;left:470px;top:0;width:730px;height:251px;
    background:linear-gradient(90deg,var(--navy) 0%,#5f7489 18%,#c9ced2 38%,#e9e9e7 52%,#3b4352 72%,#c1a58c 88%,#2c3a52 100%)}
  .hero h1{position:absolute;left:236px;top:84px;font-family:"Roboto",sans-serif;font-weight:900;font-size:38px;line-height:43px;color:#fff;letter-spacing:.5px}

  .intro{left:172px;top:391px;width:860px;font-family:"Open Sans",sans-serif;font-size:14.4px;line-height:26.5px;color:var(--ink)}

  .deck{left:216px;top:474px;width:769px;height:511px;border:1px solid #d0d0d0;background:#fff}
  .deck-title{position:absolute;left:145px;font-family:"Oswald",sans-serif;font-weight:600;line-height:1;letter-spacing:-1px}
  .deck-title.t1{top:156px;font-size:62px;color:var(--slide-blue)}
  .deck-title.t2{top:222px;font-size:62px;color:var(--slide-deep)}
  .deck-sub{position:absolute;left:146px;top:309px;font-family:"Oswald",sans-serif;font-weight:300;font-size:20px;letter-spacing:-1px;color:var(--slide-deep)}
  .deck-brand{position:absolute;left:534px;top:380px;width:144px;text-align:center;font-family:"Open Sans",sans-serif;font-weight:600;font-size:34px;color:var(--brand-blue)}
  .deck-bar{position:absolute;left:0;bottom:0;width:767px;height:32px;background:var(--bar);border-top:1px solid #ddd}
  .deck-bar .name{position:absolute;left:12px;top:9px;font-size:11px;color:#555}
  .deck-bar .page{position:absolute;right:28px;top:7px;font-size:11px;color:var(--brand-blue)}
  .deck-bar .page b{display:inline-block;width:24px;height:17px;border:1px solid #ccc;background:#fff;font-weight:400;color:#333;text-align:right;padding-right:3px;margin-right:3px;vertical-align:middle}

  .footer{left:0;top:1045px;width:1200px;height:101px;background:var(--footer);color:var(--footer-text);font-size:9.5px}
  .footer .links{position:absolute;left:174px;top:33px;word-spacing:1px}
  .footer .links i{font-style:normal;margin:0 14px}
  .footer .copy{position:absolute;left:174px;top:58px;font-size:8.5px}
  .footer .contact{position:absolute;white-space:nowrap}
</style>
</head>
<body>

<div class="abs brand"><span class="brand-mark"></span>Tolvan</div>

<div class="abs follow">FOLLOW US :</div>
<div class="abs social" style="left:878px" aria-label="Social profile"></div>
<div class="abs social" style="left:917px" aria-label="Social profile"></div>
<div class="abs social" style="left:955px" aria-label="Social profile"></div>
<div class="abs social" style="left:994px" aria-label="Social profile"></div>

<nav class="abs nav">
  <span style="left:338px">HOME</span>
  <span style="left:429px">ABOUT US</span>
  <span style="left:547px">INVEST DIFFERENTLY</span>
  <span style="left:722px">CONTENT</span>
  <span style="left:843px">CAREER</span>
  <span style="left:949px">CONTACT US</span>
</nav>

<section class="abs hero">
  <div class="hero-photo" role="img" aria-label="Photo of advisors meeting with a client at a bright office table"></div>
  <h1>INVESTMENT<br>PROCESS</h1>
</section>

<p class="abs intro">A disciplined, process-driven, value investment firm that provides a private portfolio management service tailored to individual and institutional clients tired of in-the-box, cookie-cutter, buy-and-hope investment products.</p>

<div class="abs deck">
  <svg class="abs" style="left:0;top:0" width="767" height="478">
    <line x1="121" y1="153" x2="121" y2="316" stroke="#2a3a4f" stroke-width="1.5"/>
    <line x1="105" y1="300" x2="678" y2="300" stroke="#2a3a4f" stroke-width="1.5"/>
  </svg>
  <div class="deck-title t1">ACTIVE VALUE</div>
  <div class="deck-title t2">INVESTING</div>
  <div class="deck-sub">MAKING MONEY IN THIS MARKET AND THIS ECONOMY</div>
  <div class="deck-brand">Tolvan</div>
  <div class="deck-bar">
    <span class="name">deckshelf</span>
    <svg class="abs" style="left:396px;top:4px" width="110" height="24">
      <path d="M6 8v8M15 8l-7 4 7 4z" fill="#333" stroke="#333" stroke-width="1.2"/>
      <circle cx="38" cy="12" r="11" fill="none" stroke="#333" stroke-width="1.5"/>
      <path d="M42 7l-8 5 8 5z" fill="#333"/>
      <circle cx="72" cy="12" r="11" fill="none" stroke="#333" stroke-width="1.5"/>
      <path d="M68 7l8 5-8 5z" fill="#333"/>
      <path d="M96 8l7 4-7 4zM104 8v8" fill="#333" stroke="#333" stroke-width="1.2"/>
    </svg>
    <span class="page"><b>1</b>/16</span>
    <svg class="abs" style="right:6px;top:9px" width="15" height="15">
      <path d="M1 5V1h4M10 1h4v4M14 10v4h-4M5 14H1v-4M1 1l4 4M14 1l-4 4M14 14l-4-4M1 14l4-4" fill="none" stroke="#333" stroke-width="1.6"/>
    </svg>
  </div>
</div>

<footer class="abs footer">
  <div class="links">ABOUT US<i>|</i>INVEST DIFFERENTLY<i>|</i>CONTENT<i>|</i>CAREER<i>|</i>CONTACT US</div>
  <div class="copy">© TOLVAN 2014. ALL RIGHTS RESERVED.</div>
  <svg class="abs" style="left:764px;top:30px" width="10" height="14"><rect x="1.5" y="1" width="7" height="12" rx="1.5" fill="none" stroke="#aaa" stroke-width="1.3"/></svg>
  <div class="contact" style="left:782px;top:32px">PHONE: 303.555.0148,&nbsp; 888.555.0172</div>
  <svg class="abs" style="left:762px;top:57px" width="12" height="11"><rect x="3" y="0" width="6" height="3" fill="#aaa"/><rect x="0" y="3" width="12" height="5" fill="#aaa"/><rect x="3" y="7" width="6" height="4" fill="#aaa"/></svg>
  <div class="contact" style="left:782px;top:58px">FAX: 303.555.0193</div>
  <svg class="abs" style="left:882px;top:57px" width="13" height="10"><rect x=".5" y=".5" width="12" height="9" fill="#aaa"/><path d="M.5 .5l6 5 6-5" fill="none" stroke="#000" stroke-width="1"/></svg>
  <div class="contact" style="left:903px;top:58px">EMAIL: <span style="color:#ddd">contact@tolvanfunds.example</span></div>
</footer>

</body>
</html>
```